Fernbrook Dwellings Business Card Design Project

Please create a custom Business Card Design for Fernbrook Dwellings. The logo is attached to this brief.Please include space for
Name Surname
Title (Solutions Specialist)
Phone
Email
Website
Industry/Entity Type
Business
Contact Information for Business Card
Reverse should be printed horizontally and have the following components:
Small version of the logo. (lowest priority)
The words "Real Estate Solutions Company"
A bulleted list (Note: Line breaks are suggestions only):
* BUY, RENOVATE, SELL and RENT:
RESIDENTIAL PROPERTIES
* MAKE CASH OFFERS ON HOUSES IN
ANY CONDITION and IN ANY SITUATION
* SELL PROPERTIES TO INVESTORS
* SOLVE COMPLEX REAL ESTATE
PROBLEMS and TITLE ISSUES
* PRIVATE MONEY INVESTMENT SERVICES
* PAY CASH REWARDS FOR REFERRALS
Included somewhere on the reverse should also be the following:
Office: (425) 555-0183
www.FernbrookDwellings.example
space for civic trade registry logo
Look and feel
Each slider illustrates characteristics of the customer's brand and the style your logo design should communicate.

```html
<!DOCTYPE html>
<html lang="en">
<head>
<meta charset="utf-8">
<title>Fernbrook Dwellings Business Card</title>
<link rel="stylesheet" href="https://fonts.googleapis.com/css2?family=Lato:wght@400;700;900&display=swap">
<style>
  :root {
    --backdrop: #2a2a2a;
    --card-blue: #1d73c4;
    --card-blue-deep: #135ea8;
    --card-white: #ffffff;
    --card-white-shade: #e9e9e9;
    --ink-blue: #1b5ba8;
    --ink-grey: #5a5a5a;
    --bar-grey: #6b6b6b;
    --bar-blue: #1b5ba8;
    --accent-gold: #f2b705;
    --ink-on-blue: #ffffff;
    --soft-on-blue: rgba(255, 255, 255, 0.85);
  }
  * { box-sizing: border-box; margin: 0; padding: 0; }
  html, body { width: 1200px; height: 997px; overflow: hidden; }
  body {
    background: var(--backdrop);
    font-family: "Lato", Arial, sans-serif;
    position: relative;
  }
  .card {
    position: absolute;
    width: 510px;
    height: 300px;
    border-radius: 22px;
    top: 348px;
  }

  /* Reverse (blue) */
  .card-reverse {
    left: 65px;
    background: linear-gradient(160deg, var(--card-blue), var(--card-blue-deep));
    color: var(--ink-on-blue);
    padding: 22px 26px 20px;
    display: flex;
    flex-direction: column;
  }
  .reverse-head {
    display: flex;
    align-items: center;
    justify-content: space-between;
  }
  .mini-brand {
    display: flex;
    align-items: center;
    gap: 8px;
  }
  .mini-brand .brand-dot { width: 18px; height: 18px; }
  .mini-brand .brand-name { font-size: 15px; font-weight: 900; letter-spacing: 1px; text-transform: uppercase; }
  .tagline {
    margin-top: 14px;
    font-size: 17px;
    font-weight: 900;
    letter-spacing: 0.5px;
    text-transform: uppercase;
  }
  .services {
    margin-top: 12px;
    list-style: none;
    display: flex;
    flex-direction: column;
    gap: 5px;
  }
  .services li {
    position: relative;
    padding-left: 14px;
    font-size: 11px;
    font-weight: 700;
    line-height: 1.3;
    color: var(--soft-on-blue);
  }
  .services li::before {
    content: "";
    position: absolute;
    left: 0;
    top: 4px;
    width: 6px;
    height: 6px;
    border-radius: 50%;
    background: var(--accent-gold);
  }
  .reverse-foot {
    margin-top: auto;
    display: flex;
    align-items: flex-end;
    justify-content: space-between;
    border-top: 1px solid rgba(255, 255, 255, 0.35);
    padding-top: 10px;
  }
  .office { font-size: 12px; font-weight: 700; line-height: 1.4; }
  .registry-badge {
    width: 40px;
    height: 40px;
    border-radius: 6px;
    background: rgba(255, 255, 255, 0.9);
  }

  /* Front (white) */
  .card-front {
    left: 625px;
    background: linear-gradient(150deg, var(--card-white) 55%, var(--card-white-shade));
  }
  .brand-dot {
    display: block;
    border-radius: 50%;
    background: var(--accent-gold);
  }
  .card-front .brand {
    position: absolute;
    right: 30px;
    top: 62px;
    width: 190px;
    display: flex;
    flex-direction: column;
    align-items: center;
    gap: 14px;
  }
  .card-front .brand-dot { width: 36px; height: 36px; }
  .card-front .brand-name {
    color: var(--ink-blue);
    font-size: 24px;
    font-weight: 900;
    letter-spacing: 1px;
    text-transform: uppercase;
    text-align: center;
    line-height: 1.1;
  }
  .contact {
    position: absolute;
    left: 32px;
    top: 50px;
    display: flex;
    flex-direction: column;
    gap: 28px;
  }
  .contact-group {
    border-left: 5px solid var(--bar-grey);
    padding-left: 10px;
    line-height: 1.25;
  }
  .contact-group.numbers { border-left-color: var(--bar-blue); }
  .person-name { color: var(--ink-blue); font-weight: 900; font-size: 17px; }
  .person-title { color: var(--ink-blue); font-weight: 400; font-size: 13px; }
  .address { color: var(--ink-blue); font-weight: 700; font-size: 14px; }
  .detail { color: var(--ink-grey); font-weight: 700; font-size: 14px; }
</style>
</head>
<body>
  <section class="card card-reverse" aria-label="Card reverse">
    <div class="reverse-head">
      <div class="mini-brand">
        <span class="brand-dot"></span>
        <span class="brand-name">Fernbrook Dwellings</span>
      </div>
    </div>
    <p class="tagline">Real Estate Solutions Company</p>
    <ul class="services">
      <li>BUY, RENOVATE, SELL and RENT: RESIDENTIAL PROPERTIES</li>
      <li>MAKE CASH OFFERS ON HOUSES IN ANY CONDITION and IN ANY SITUATION</li>
      <li>SELL PROPERTIES TO INVESTORS</li>
      <li>SOLVE COMPLEX REAL ESTATE PROBLEMS and TITLE ISSUES</li>
      <li>PRIVATE MONEY INVESTMENT SERVICES</li>
      <li>PAY CASH REWARDS FOR REFERRALS</li>
    </ul>
    <div class="reverse-foot">
      <div class="office">
        <p>Office: (425) 555-0183</p>
        <p>www.FernbrookDwellings.example</p>
      </div>
      <span class="registry-badge" role="img" aria-label="Space for civic trade registry badge"></span>
    </div>
  </section>

  <section class="card card-front" aria-label="Card front">
    <div class="contact">
      <div class="contact-group">
        <p class="person-name">MARTIN ASHBY</p>
        <p class="person-title">Solutions Specialist</p>
        <p class="detail">www.ashbyfernbrook.example</p>
      </div>
      <div class="contact-group">
        <p class="address">14 Alder Row, Millbrook,<br>Westshire WS4 2QT, UK</p>
      </div>
      <div class="contact-group numbers">
        <p class="detail">+44 20 7946 0321</p>
        <p class="detail">+44 20 7946 0874</p>
        <p class="detail">post@ashbyfernbrook.example</p>
      </div>
    </div>
    <div class="brand">
      <span class="brand-dot"></span>
      <span class="brand-name">Fernbrook<br>Dwellings</span>
    </div>
  </section>
</body>
</html>
```